Review Site Redesign

We have a rather ambitious goal to reinvent (redesign) the way bank financial review sites present information. In that respect, we’re looking for an innovative creative design.
As examples of what I would call bad or boring design please look at the following sites:
1. http://brisklend.example/se
2. http://vantorquay.example/se/privatlan
3. http://glimsworth.example/no
These are the traditional way these types of review sites are organized: dull and boring. I think we can do a lot better than that.
I need a site that will capture attention end engage the visitor; a site that will create a more interactive and less passive user experience.
Scope of work should also include logo font and additional content space for articles, FAQ, widgets, social media links, etc.

Not sure what to advise you as best format - maybe a flash or js carousel, gallery, wheel, logo image matrix, or something else.
Maybe some kind of interactive logo matrix such as this site: http://www.quarnibo.example/
Please apply your best creative mind work to this problem.
Also, please think about creative use of background images, stock photos, etc.
For logo font use can use URL “pellrowatt.example” as placeholder.

```html
<!DOCTYPE html>
<html lang="no">
<head>
<meta charset="utf-8">
<title>Pellrowatt – Sammenlign lån</title>
<link href="https://fonts.googleapis.com/css2?family=Oswald:wght@300;400;500&family=PT+Sans+Narrow:wght@400;700&display=swap" rel="stylesheet">
<style>
:root{
  --yellow:#f6b800;
  --yellow-dark:#e0a400;
  --ink:#2b2b2b;
  --text:#4a4a4a;
  --muted:#8a8a8a;
  --panel:#d9d9d9;
  --steel-1:#8d8d8d;
  --steel-2:#c9c9c9;
  --steel-3:#efefef;
  --white:#ffffff;
  --dark:#3a3a3a;
}
*{box-sizing:border-box;margin:0;padding:0}
html,body{width:667px;height:1200px;overflow:hidden}
body{
  position:relative;
  font-family:"PT Sans Narrow",Arial,sans-serif;
  color:var(--text);
  background:linear-gradient(90deg,var(--steel-1) 0%,var(--steel-2) 15%,var(--steel-3) 32%,var(--steel-2) 48%,var(--steel-3) 62%,var(--steel-2) 80%,var(--steel-1) 100%);
}
.abs{position:absolute}

/* brand */
.brand{left:58px;top:6px;width:90px;text-align:center}
.brand-mark{width:62px;height:62px;border-radius:50%;background:var(--yellow);margin:0 auto;border:2px solid var(--white)}
.brand-name{font-family:"Oswald",sans-serif;font-weight:400;font-size:11px;color:var(--ink);margin-top:2px;letter-spacing:.3px}

/* navigation */
.main-nav{left:56px;top:86px;width:555px;height:25px;background:var(--yellow);display:flex;border-top:1px solid var(--yellow-dark)}
.main-nav a{flex:1;text-align:center;font-family:"Oswald",sans-serif;font-size:9.5px;line-height:24px;color:var(--ink);text-decoration:none;border-right:1px solid var(--yellow-dark)}
.main-nav a:last-child{border-right:0}

/* hero */
.hero{left:56px;top:111px;width:555px;height:236px;background:linear-gradient(100deg,#e9eaea 0%,#b8bcbf 30%,#8a7a6e 55%,#cfd3d4 80%,#eef0f0 100%)}
.hero-caption{left:6px;top:80px;width:202px;padding:6px 8px;background:rgba(40,40,40,.78);font-family:"Oswald",sans-serif;font-size:9.2px;line-height:15px;color:var(--white)}
.hero-dots{right:8px;bottom:6px;display:flex;gap:4px}
.hero-dots span{width:6px;height:6px;border-radius:50%;background:var(--yellow)}
.hero-dots span:first-child{background:var(--ink)}

/* quick loan band */
.headline-band{left:56px;top:347px;width:555px;height:31px;background:var(--yellow);font-family:"Oswald",sans-serif;font-size:13.4px;line-height:31px;padding-left:9px;color:var(--ink);white-space:nowrap;overflow:hidden}
.headline-band strong{font-weight:500}

/* loan comparison */
.compare{left:56px;top:378px;width:555px;height:244px;background:#ececec;border-radius:0 0 6px 6px}
.tabs{left:7px;top:9px;width:541px;height:18px;display:flex}
.tabs span{flex:1;text-align:center;font-family:"Oswald",sans-serif;font-size:9px;line-height:18px;color:var(--ink)}
.tabs .active{background:var(--yellow);color:var(--white);flex:.8}
.loan-table{left:7px;top:27px;width:541px;height:210px;background:var(--white);overflow:hidden}
.loan-head{height:23px;background:linear-gradient(#5a5a5a,#3b3b3b);font-size:8.5px;line-height:23px;color:var(--yellow);position:relative}
.loan-head span,.loan-row .cell{position:absolute}
.c-logo{left:14px}.c-info{left:60px}.c-sum{left:200px}.c-time{left:290px}.c-open{left:348px}
.loan-row{position:relative;height:74px;border-bottom:1px solid #e3e3e3;font-size:7.6px;line-height:13px;color:var(--text)}
.loan-row .c-logo{left:4px;top:10px;width:50px;height:46px;display:flex;align-items:center;justify-content:center;font-family:"Oswald",sans-serif;font-size:10px;color:var(--ink);background:#f7f7f7}
.loan-row .c-info{left:60px;top:6px;width:130px}
.loan-row .c-sum{top:6px}.loan-row .c-time{top:6px}
.loan-row .c-open{top:6px;width:110px}
.more{color:var(--yellow)}
.apply{left:464px;top:18px;width:42px;height:42px;border-radius:50%;background:var(--dark);border:3px solid #bdbdbd;color:var(--yellow);font-family:"Oswald",sans-serif;font-size:7px;line-height:36px;text-align:center}
.scrollbar{right:0;top:23px;width:9px;height:187px;background:#efefef;border-left:1px solid #ddd}
.scrollbar::after{content:"";position:absolute;left:1px;top:6px;width:6px;height:60px;border-radius:3px;background:#c4c4c4}

/* content */
.content{left:56px;top:629px;width:555px;height:472px;background:var(--white);border-radius:6px}
.ribbon{left:-9px;width:114px;height:17px;background:var(--yellow);font-family:"Oswald",sans-serif;font-size:10.5px;line-height:17px;color:var(--white);padding-left:13px;clip-path:polygon(0 0,92% 0,100% 50%,92% 100%,0 100%)}
.articles{left:6px;top:32px;width:256px;height:286px;overflow:hidden}
.article{padding-bottom:5px;margin-bottom:5px;border-bottom:1px dashed #bdbdbd}
.article h3,.faq-item h3{font-family:"PT Sans Narrow",sans-serif;font-weight:400;font-size:10px;line-height:14px;color:var(--ink);margin-bottom:1px}
.article p,.faq-item p{font-size:7px;line-height:13px;letter-spacing:-.05px}
.article .meta{font-size:7px;color:var(--muted);margin-top:3px}
.meta span{margin:0 7px}
.faq{left:6px;top:346px;width:256px}
.faq-item{margin-bottom:4px;padding-bottom:2px}
.faq-item:first-child{border-bottom:1px dashed #bdbdbd}
.widget{left:313px;width:237px;background:var(--panel);text-align:center;font-family:"Oswald",sans-serif;font-size:16px;color:var(--yellow);padding-top:9px}

/* footer */
.site-footer{left:56px;top:1108px;width:555px;height:48px;background:var(--yellow);border-radius:0 0 6px 6px}
.footer-nav{left:0;top:0;width:355px;height:48px;display:flex;align-items:center;justify-content:space-around;padding:0 4px}
.footer-nav a{font-family:"Oswald",sans-serif;font-size:7.5px;color:var(--ink);text-decoration:none}
.follow{left:355px;top:7px;width:200px;height:34px;background:var(--dark);border-radius:4px 0 0 4px;display:flex;align-items:center;padding-left:14px;gap:7px;font-family:"Oswald",sans-serif;font-size:7px;color:var(--white)}
.follow .label{margin-right:8px}
.follow .circle{width:18px;height:18px;border-radius:50%;border:2px solid #6b6b6b}
.copyright{left:0;top:1166px;width:667px;text-align:center;font-family:"Oswald",sans-serif;font-size:7px;color:var(--white)}
</style>
</head>
<body>

<div class="abs brand">
  <div class="brand-mark"></div>
  <div class="brand-name">Pellrowatt</div>
</div>

<nav class="abs main-nav">
  <a href="#">HEM</a><a href="#">ALLT OM EKONOMI</a><a href="#">EKONOMI ORDBOK</a><a href="#">OM OSS</a><a href="#">KONTAKT</a><a href="#">FORUM</a>
</nav>

<section class="abs hero" role="img" aria-label="Foto: et smilende par som omfavner hverandre foran en bærbar datamaskin">
  <p class="abs hero-caption">GLIMSWORTH SAMMENLIGNER OG VURDERER ONLINE LÅN. FORMÅLET ER, Å GI DEG SOM BRUKER MULIGHETEN FOR Å FINNE ET LÅN, SOM PASSER TIL NETTOPP DINE BEHOV.</p>
  <div class="abs hero-dots"><span></span><span></span><span></span><span></span><span></span></div>
</section>

<div class="abs headline-band"><strong>SÅ LÅNAR DU PENGAR DIREKT</strong> &nbsp;: Ibland kan man hamna i en situation där man behöver låna pengar direkt.</div>

<section class="abs compare">
  <div class="abs tabs">
    <span class="active">ALLE LÅN</span><span>SMÅLÅN</span><span>STORE LÅN</span><span>FORBRUKSLÅN</span><span>KREDITTKORT</span><span>FAVORITTLÅN</span><span>NYHETER</span>
  </div>
  <div class="abs loan-table">
    <div class="loan-head">
      <span class="c-logo">Lån</span><span class="c-info">Informasjon</span><span class="c-sum">Beløp</span><span class="c-time">Løpetid</span><span class="c-open">Åpen for</span>
    </div>
    <div class="loan-row">
      <div class="cell c-logo">Lumora</div>
      <div class="cell c-info">FORBRUKSLÅN. Anders fra Lumora hjelper deg med små og store lån. Eks. 25.000, 29,33% eff., 25.000 o/5 år, geb. 785, tot. 44.878.<br><span class="more">LES MER</span></div>
      <div class="cell c-sum">5.000 - 25.000</div>
      <div class="cell c-time">1-5 år</div>
      <div class="cell c-open">Fylt 20 år. Fast inntekt. Ingen betalingsanm.</div>
      <div class="abs apply">SØK HER</div>
    </div>
    <div class="loan-row">
      <div class="cell c-logo">Brevik</div>
      <div class="cell c-info">FORBRUKSLÅN. Anders fra Lumora hjelper deg med små og store lån. Eks. 25.000, 29,33% eff., 25.000 o/5 år, geb. 785, tot. 44.878.<br><span class="more">LES MER</span></div>
      <div class="cell c-sum">5.000 - 25.000</div>
      <div class="cell c-time">1-5 år</div>
      <div class="cell c-open">Fylt 20 år. Fast inntekt. Ingen betalingsanm.</div>
      <div class="abs apply">SØK HER</div>
    </div>
    <div class="loan-row">
      <div class="cell c-logo">Tollund</div>
      <div class="cell c-info">FORBRUKSLÅN. Anders fra Lumora hjelper deg med små og store lån. Eks. 25.000.</div>
      <div class="cell c-sum">5.000 - 25.000</div>
      <div class="cell c-time">1-5 år</div>
      <div class="cell c-open">Fylt 20 år. Fast inntekt. Ingen betalingsanm.</div>
      <div class="abs apply">SØK HER</div>
    </div>
    <div class="abs scrollbar"></div>
  </div>
</section>

<main class="abs content">
  <div class="abs ribbon" style="top:10px">LATEST ARTICLES</div>
  <div class="abs articles">
    <article class="article">
      <h3>Slik låner du penger</h3>
      <p>Det er ekstremt lett å låne penger bare for å gjøre hverdagen litt søtere. Det kan gjøres i løpet av 5 minutter på hjemmesiden til låneutbyderne. Du trenger bare å fylle inn dine private opplysninger og kontoopplysninger, velge lånebeløp og hvordan du vil dele opp avdragene. Når der er gjort, kan du slappe av og lene deg tilbake mens du venter på at din søknad om å låne penger blir vurdert.</p>
      <p class="meta">Author: admin<span>|</span>Posted in Slik låner du penger</p>
    </article>
    <article class="article">
      <h3>Slik låner du penger</h3>
      <p>Det er ekstremt lett å låne penger bare for å gjøre hverdagen litt søtere. Det kan gjøres i løpet av 5 minutter på hjemmesiden til låneutbyderne. Du trenger bare å fylle inn dine private opplysninger og kontoopplysninger, velge lånebeløp og hvordan du vil dele opp avdragene. Når der er gjort, kan du slappe av og lene deg tilbake mens du venter på at din søknad om å låne penger blir vurdert.</p>
      <p class="meta">Author: admin<span>|</span>Posted in Slik låner du penger</p>
    </article>
    <article class="article" style="border-bottom:0">
      <h3>Slik låner du penger</h3>
      <p>Det er ekstremt lett å låne penger bare for å gjøre hverdagen litt søtere. Det kan gjøres i løpet av 5 minutter på hjemmesiden til låneutbyderne. Du trenger bare å fylle inn dine private opplysninger og kontoopplysninger, velge lånebeløp og hvordan du vil dele opp avdragene. Når der er gjort, kan du slappe av og lene deg tilbake mens du venter på at din søknad om å låne penger blir vurdert.</p>
      <p class="meta">Author: admin<span>|</span>Posted in Slik låner du penger</p>
    </article>
  </div>

  <div class="abs ribbon" style="top:323px">FAQ</div>
  <div class="abs faq">
    <div class="faq-item">
      <h3>Søk online hos en godkjent utbyder ?</h3>
      <p>Du kan søke om lån hos utbyderne over. Alle er godkjente til å drive med lånevirksomhet i Norge, så du kan være sikker på at du får et lån med ordentlige og rettferdige vilkår. Klikk på linken og søk online på utbydernes hjemmesider.</p>
    </div>
    <div class="faq-item">
      <h3>Søk online hos en godkjent utbyder ?</h3>
      <p>Du kan søke om lån hos utbyderne over. Alle er godkjente til å drive med lånevirksomhet i Norge, så du kan være sikker på at du får et lån med ordentlige og rettferdige vilkår. Klikk på linken og søk online på utbydernes hjemmesider.</p>
    </div>
  </div>

  <aside class="abs widget" style="top:7px;height:203px">WIDGETS</aside>
  <aside class="abs widget" style="top:240px;height:212px">WIDGETS</aside>
</main>

<footer class="abs site-footer">
  <nav class="abs footer-nav">
    <a href="#">HEM</a><a href="#">ALLT OM EKONOMI</a><a href="#">EKONOMI ORDBOK</a><a href="#">OM OSS</a><a href="#">KONTAKT</a><a href="#">FORUM</a>
  </nav>
  <div class="abs follow">
    <span class="label">FOLLOW US ON :</span>
    <span class="circle"></span><span class="circle"></span><span class="circle"></span><span class="circle"></span>
  </div>
</footer>

<p class="abs copyright">COPYRIGHT © PELLROWATT 2012 - ALL RIGHTS RESERVED</p>

</body>
</html>
```